New Business Card Design Project

Want a simple but attention grabbing business card. Back Side having mainly our logo and basic info-the front side a typical business card.

Contact Information for Business Card

Hearth & Tile Interiors
218 NW Larkspur Rd. Suite 207
Ankeny, Iowa 50021

phone- 515.482.7093

website is -htidesigns.com

```html
<!DOCTYPE html>
<html lang="en">
<head>
<meta charset="utf-8">
<title>Hearth &amp; Tile Interiors – Business Card</title>
<link rel="stylesheet" href="https://fonts.googleapis.com/css2?family=Montserrat:wght@700&family=Open+Sans:wght@400;600&display=swap">
<style>
  :root {
    --stage: #1c1d20;
    --card: #0b1628;
    --edge: #f0591f;
    --orange: #f26522;
    --blue: #2f7fd1;
    --muted-blue: #355879;
    --ink: #e9edf3;
  }
  * { box-sizing: border-box; margin: 0; padding: 0; }
  html, body { width: 1200px; height: 839px; overflow: hidden; }
  body {
    background: var(--stage);
    font-family: "Open Sans", sans-serif;
    display: flex;
    justify-content: center;
    align-items: center;
    gap: 110px;
  }
  .card {
    width: 360px;
    height: 630px;
    background: var(--card);
    border-radius: 22px;
    border-bottom: 3px solid var(--edge);
    border-left: 2px solid var(--edge);
    position: relative;
  }
  /* back side */
  .card-back {
    display: flex;
    align-items: center;
    justify-content: center;
  }
  .back-name {
    font-weight: 600;
    font-size: 27px;
    line-height: 1.25;
    color: var(--muted-blue);
    text-align: center;
  }
  /* front side */
  .card-front { padding: 70px 34px 0; }
  .brand {
    font-weight: 600;
    font-size: 24px;
    line-height: 1.2;
    color: var(--orange);
    text-align: center;
  }
  .person { margin-top: 200px; }
  .person-name {
    font-family: "Montserrat", sans-serif;
    font-weight: 700;
    font-size: 22px;
    letter-spacing: 0.5px;
    color: var(--orange);
  }
  .person-role { font-size: 15px; color: var(--ink); margin-top: 2px; }
  .address { font-size: 14.5px; color: var(--ink); margin-top: 26px; line-height: 1.5; }
  .contacts { list-style: none; margin-top: 26px; }
  .contacts li {
    display: flex;
    align-items: center;
    gap: 9px;
    font-size: 14.5px;
    color: var(--ink);
    line-height: 1.65;
  }
  .contacts svg { width: 13px; height: 13px; fill: var(--blue); flex: none; }
</style>
</head>
<body>
  <section class="card card-back" aria-label="Card back">
    <p class="back-name">Hearth &amp; Tile<br>Interiors</p>
  </section>

  <section class="card card-front" aria-label="Card front">
    <p class="brand">Hearth &amp; Tile Interiors</p>

    <div class="person">
      <p class="person-name">DALE WHITMORE</p>
      <p class="person-role">President</p>
    </div>

    <p class="address">218 NW Larkspur Rd. Suite 207<br>Ankeny, Iowa 50021</p>

    <ul class="contacts">
      <li>
        <svg viewBox="0 0 24 24" aria-hidden="true"><path d="M6.6 10.8a15.2 15.2 0 0 0 6.6 6.6l2.2-2.2c.3-.3.7-.4 1-.2 1.1.4 2.3.6 3.6.6.6 0 1 .4 1 1V20c0 .6-.4 1-1 1A17 17 0 0 1 3 4c0-.6.4-1 1-1h3.5c.6 0 1 .4 1 1 0 1.3.2 2.5.6 3.6.1.3 0 .7-.2 1z"/></svg>
        515.482.7093
      </li>
      <li>
        <svg viewBox="0 0 24 24" aria-hidden="true"><path d="M2 5h20v14H2z M2 5l10 8 10-8" /></svg>
        info@htidesigns.com
      </li>
      <li>
        <svg viewBox="0 0 24 24" aria-hidden="true"><circle cx="12" cy="12" r="10"/></svg>
        www.htidesigns.com
      </li>
    </ul>
  </section>
</body>
</html>
```